Storm Restoration Contractor needs a professional business card design

Looking for a professional business card design. Not looking for your cheapo MS Word standard ones that are readily available. Dont want it to be cookie cutter look like ones readily available online. We just recently changed our logo and want to freshen up all our documents. Our company handles restoring a property back to a pre-loss condition after a storm damages it. For example, wind, hail, flood, fire losses.

Target Market(s)

Property Owners, Homeowners, Property Owners, Commercial Property Owners, Property Management Companies, Hail and Wind Damaged Properties

Industry/Entity Type

Construction Company

Contact Information for Business Card

Brightline Facades
847-555-0193
847-555-0147 fax
www.brightlinefacades.example
info@brightlinefacades.example

Requirements
Must have
• Clean, Professional, fresh look
• Storm Restoration, Roofing, Siding, Windows
Nice to have
• If there is a way to incorporate storms that may be cool.

```html
<!DOCTYPE html>
<html lang="en">
<head>
<meta charset="utf-8">
<title>Brightline Facades – Business Card</title>
<link rel="stylesheet" href="https://fonts.googleapis.com/css2?family=Arimo:wght@400;700&display=swap">
<style>
  :root {
    --backdrop: #b4b4b4;
    --card: #f7f7f7;
    --brand-blue: #2f80c9;
    --ink-grey: #5a5a5a;
    --ink-soft: #6b6b6b;
  }
  html, body {
    margin: 0;
    padding: 0;
    width: 1200px;
    height: 1200px;
    overflow: hidden;
    background: var(--backdrop);
    font-family: "Arimo", Arial, sans-serif;
  }
  .card {
    position: absolute;
    left: 75px;
    top: 300px;
    width: 1050px;
    height: 600px;
    background: var(--card);
    box-shadow: 0 6px 24px rgba(0,0,0,0.18);
  }
  .brand {
    position: absolute;
    right: 90px;
    top: 70px;
    display: flex;
    flex-direction: column;
    align-items: center;
    gap: 22px;
  }
  .brand-mark {
    width: 130px;
    height: 130px;
    border-radius: 50%;
    border: 9px solid var(--brand-blue);
    box-sizing: border-box;
  }
  .brand-name {
    font-weight: 700;
    font-size: 30px;
    letter-spacing: 3px;
    text-transform: uppercase;
    color: var(--brand-blue);
  }
  .person {
    position: absolute;
    left: 180px;
    top: 318px;
  }
  .person-name {
    font-size: 40px;
    color: var(--ink-grey);
    line-height: 1.05;
  }
  .person-role {
    font-size: 24px;
    color: var(--brand-blue);
    margin-top: 2px;
  }
  .contact-list {
    position: absolute;
    left: 180px;
    top: 430px;
    list-style: none;
    margin: 0;
    padding: 0;
  }
  .contact-item {
    display: flex;
    align-items: center;
    gap: 14px;
    font-size: 22px;
    color: var(--ink-grey);
    height: 32px;
  }
  .contact-icon {
    width: 22px;
    height: 22px;
    flex: none;
  }
</style>
</head>
<body>
  <section class="card">
    <div class="brand">
      <div class="brand-mark"></div>
      <div class="brand-name">Brightline Facades</div>
    </div>

    <div class="person">
      <div class="person-name">Daniel Reyes</div>
      <div class="person-role">Owner</div>
    </div>

    <ul class="contact-list">
      <li class="contact-item">
        <svg class="contact-icon" viewBox="0 0 22 22" aria-hidden="true">
          <rect width="22" height="22" rx="2" fill="#2f80c9"/>
          <path d="M7 5 L9.5 5 L10.5 8 L9 9.2 C9.8 11 11 12.2 12.8 13 L14 11.5 L17 12.5 L17 15 C17 16 16 16.8 15 16.7 C9.8 16.2 5.8 12.2 5.3 7 C5.2 6 6 5 7 5 Z" fill="#fff"/>
        </svg>
        <span>847-555-0193</span>
      </li>
      <li class="contact-item">
        <svg class="contact-icon" viewBox="0 0 22 22" aria-hidden="true">
          <rect width="22" height="22" rx="2" fill="#2f80c9"/>
          <rect x="7" y="4" width="8" height="5" fill="#fff"/>
          <rect x="4" y="9" width="14" height="7" rx="1" fill="#fff"/>
          <rect x="7" y="14" width="8" height="4" fill="#fff" stroke="#2f80c9" stroke-width="1"/>
        </svg>
        <span>847-555-0147</span>
      </li>
      <li class="contact-item">
        <svg class="contact-icon" viewBox="0 0 22 22" aria-hidden="true">
          <rect width="22" height="22" rx="2" fill="#2f80c9"/>
          <rect x="4" y="6" width="14" height="10" fill="#fff"/>
          <path d="M4 6 L11 12 L18 6" fill="none" stroke="#2f80c9" stroke-width="1.5"/>
        </svg>
        <span>info@brightlinefacades.example</span>
      </li>
      <li class="contact-item">
        <svg class="contact-icon" viewBox="0 0 22 22" aria-hidden="true">
          <rect width="22" height="22" rx="2" fill="#2f80c9"/>
          <circle cx="11" cy="11" r="6.5" fill="none" stroke="#fff" stroke-width="1.6"/>
          <ellipse cx="11" cy="11" rx="2.8" ry="6.5" fill="none" stroke="#fff" stroke-width="1.3"/>
          <line x1="4.5" y1="11" x2="17.5" y2="11" stroke="#fff" stroke-width="1.3"/>
        </svg>
        <span>www.brightlinefacades.example</span>
      </li>
    </ul>
  </section>
</body>
</html>
```